Audio Visual company needs brochure design

We are an AV company that does Audio Visual work solely for Commercial customers. We Design, sale and install various Audio Visual systems for our customers. This may be something as simple as a conference room, a new sound system for a church or a new sound, lighting and video system for an arena or stadium.

We don't really have any ideas in mind and that's the reason we are turning to you. We want something that highlights what we do, and something they will look at - not just toss in the can.

Included is a copy of our logo (sorry it's the only copy we have now)

Our company name is Kelvara Productions www.kelvaraproductions.com

Reason: The rest of our management team hasn't provided feedback to me yet. We will pick the design this week.

Target Market(s)

70% of our business is churches and the remaining is corporate customers and restaurants.

Industry/Entity Type

Church

Requirements
Must have
• The brochure will be 8.5" x 11" printed both sides - open to Z fold or Tri fold designs. We can provide pictures of our work if needed - though they may not be the best.
Should not have
• No generic pictures of just speakers, projectors, microphones, etc.

```html
<!DOCTYPE html>
<html lang="en">
<head>
<meta charset="utf-8">
<title>Kelvara Productions – Brochure Inside Panels</title>
<link rel="stylesheet" href="https://fonts.googleapis.com/css2?family=Play:wght@400;700&family=Arimo:wght@400;700&display=swap">
<style>
  :root {
    --bg-top: #3a3a3a;
    --bg-mid: #8f8f8f;
    --bg-low: #a6a6a6;
    --text: #ffffff;
    --accent: #f2c21b;
    --caption: #f0b400;
    --band: #000000;
    --stripe-blue: #2a6fd6;
    --stripe-green: #5cc43c;
    --stripe-orange: #f08a1a;
    --stripe-red: #d8342a;
    --stripe-yellow: #f3d21f;
    --stripe-cyan: #3cc7d8;
  }
  * { margin: 0; padding: 0; box-sizing: border-box; }
  html, body { width: 1200px; height: 927px; overflow: hidden; background: #ffffff; }
  .brochure {
    position: relative;
    width: 1200px;
    height: 927px;
    overflow: hidden;
    background: linear-gradient(180deg, var(--bg-top) 0%, #5a5a5a 25%, var(--bg-mid) 58%, var(--bg-low) 75%);
    font-family: "Arimo", Arial, sans-serif;
    color: var(--text);
  }
  .panel-heading {
    position: absolute;
    top: 38px;
    width: 300px;
    height: 40px;
  }
  .panel-heading svg { position: absolute; left: 0; top: 6px; }
  .panel-heading h2 {
    position: absolute;
    left: 42px;
    top: 2px;
    font-family: "Play", sans-serif;
    font-weight: 400;
    font-size: 25px;
    letter-spacing: 0.2px;
    color: var(--text);
    text-shadow: 0 0 2px rgba(0,0,0,0.4);
  }
  .column {
    position: absolute;
    top: 89px;
    width: 328px;
    font-size: 15.2px;
    line-height: 25.8px;
  }
  .column p { margin-bottom: 25.8px; }
  .column.justified p { text-align: justify; }
  .column h3 {
    font-weight: 700;
    font-size: 20px;
    line-height: 28px;
    color: var(--accent);
    margin-bottom: 10px;
  }
  .col-about { left: 40px; }
  .col-expertise { left: 442px; }
  .col-experience { left: 835px; width: 328px; }
  .col-experience h3 { margin-bottom: 16px; }
  .col-expertise p { margin-bottom: 10px; }
  .col-experience .lead { margin-bottom: 14px; }
  .photos { position: absolute; left: 0; top: 560px; }
  .caption-band {
    position: absolute;
    left: 0; top: 892px;
    width: 1200px; height: 35px;
    background: var(--band);
    display: flex;
  }
  .caption-band span {
    width: 400px;
    text-align: center;
    font-family: "Play", sans-serif;
    font-size: 17px;
    line-height: 35px;
    color: var(--caption);
    text-transform: uppercase;
  }
</style>
</head>
<body>
<main class="brochure">

  <header class="panel-heading" style="left:0">
    <svg width="270" height="28" aria-hidden="true">
      <rect x="0" y="14" width="150" height="3" fill="var(--stripe-orange)"/>
      <rect x="20" y="8" width="160" height="3" fill="var(--stripe-blue)"/>
      <rect x="10" y="20" width="255" height="3" fill="var(--stripe-yellow)"/>
      <rect x="60" y="4" width="120" height="2" fill="var(--stripe-green)"/>
      <rect x="120" y="11" width="140" height="2" fill="var(--stripe-red)"/>
      <rect x="30" y="24" width="200" height="2" fill="var(--stripe-cyan)"/>
    </svg>
    <h2>About Us</h2>
  </header>

  <header class="panel-heading" style="left:393px">
    <svg width="270" height="28" aria-hidden="true">
      <rect x="0" y="14" width="150" height="3" fill="var(--stripe-orange)"/>
      <rect x="20" y="8" width="160" height="3" fill="var(--stripe-blue)"/>
      <rect x="10" y="20" width="255" height="3" fill="var(--stripe-yellow)"/>
      <rect x="60" y="4" width="120" height="2" fill="var(--stripe-green)"/>
      <rect x="120" y="11" width="140" height="2" fill="var(--stripe-red)"/>
      <rect x="30" y="24" width="200" height="2" fill="var(--stripe-cyan)"/>
    </svg>
    <h2 style="left:50px">Expertise</h2>
  </header>

  <header class="panel-heading" style="left:798px">
    <svg width="270" height="28" aria-hidden="true">
      <rect x="0" y="14" width="150" height="3" fill="var(--stripe-orange)"/>
      <rect x="20" y="8" width="160" height="3" fill="var(--stripe-blue)"/>
      <rect x="10" y="20" width="255" height="3" fill="var(--stripe-yellow)"/>
      <rect x="60" y="4" width="120" height="2" fill="var(--stripe-green)"/>
      <rect x="120" y="11" width="140" height="2" fill="var(--stripe-red)"/>
      <rect x="30" y="24" width="200" height="2" fill="var(--stripe-cyan)"/>
    </svg>
    <h2 style="left:50px">Experience</h2>
  </header>

  <section class="column col-about justified">
    <p>A Christian owned and operated company, Kelvara Productions has been growing leaps and bounds thanks to customers like you. With an approach like none other and experience to match, Kelvara has mastered the art of providing the services our clients want, within budget and on time!</p>
    <p>Head quartered in Lakemont, Ohio, Kelvara Productions is a well established, respected and growing AV company. We have been serving the sound and lighting needs of our clients for years and look to be your partner too! We employ some of the finest engineers and technicians on a permanent basis; thus making our expertise and experience readily available from our 'in-house' engineering staff. We keep up on the latest technology and trends with a fresh inventory.</p>
  </section>

  <section class="column col-expertise justified">
    <h3>Design &amp; Installation</h3>
    <p>Our design &amp; installation team accounts for a large portion of our business. With some of the best in the country on our staff, Kelvara has become a premier systems integration company. Clients like Harwell Bancorp, Brayden Capital, Novalto &amp; Burgerly have called on Kelvara to design and install AV systems critical to their day to day operations.</p>
    <h3>Production &amp; Rentals</h3>
    <p>Serving the concert, theater and corporate markets, Kelvara provides Sound, Lighting, Video &amp; Staging services for our clients events. We have a rental department that is second to none with reasonable rates, a large inventory and a knowledgeable rental staff. Contact us and see why companies like Orvane Motors &amp; TL Magazine trust their image in our hands.</p>
  </section>

  <section class="column col-experience">
    <h3>Experience</h3>
    <p class="lead">From preschoolers to pop-starts, our diverse experience insures that every show is a success!</p>
    <h3>Creativity</h3>
    <p style="text-align:justify">Our knowledgeable staff of engineers and technicians can assist you in reaching a higher level of excitement in your shows by working with you, thinking outside of the box and having a no cookie cutter approach.</p>
    <p style="text-align:justify">We are ready to help you produce your next show. Our clients continue to use our services time after time because they know we deliver on time and within budget. Let us do the same with you. Our company is built on a strong foundation with clients like you!</p>
  </section>

  <svg class="photos" width="1200" height="332" viewBox="0 0 1200 332">
    <defs>
      <radialGradient id="indoor-tone" cx="45%" cy="30%" r="80%">
        <stop offset="0" stop-color="#c9d8ff"/>
        <stop offset="0.35" stop-color="#3d5aa8"/>
        <stop offset="1" stop-color="#0c1230"/>
      </radialGradient>
      <linearGradient id="outdoor-tone" x1="0" y1="0" x2="0" y2="1">
        <stop offset="0" stop-color="#5a4a3a"/>
        <stop offset="0.3" stop-color="#4f9a3c"/>
        <stop offset="0.55" stop-color="#7a8a6a"/>
        <stop offset="1" stop-color="#a08470"/>
      </linearGradient>
      <linearGradient id="church-tone" x1="0" y1="0" x2="0" y2="1">
        <stop offset="0" stop-color="#d8d4c8"/>
        <stop offset="0.6" stop-color="#bfae92"/>
        <stop offset="1" stop-color="#3a3632"/>
      </linearGradient>
    </defs>
    <polygon role="img" aria-label="Photo: stage lights and band performing at an indoor concert" points="0,8 402,108 402,332 0,332" fill="url(#indoor-tone)"/>
    <polygon role="img" aria-label="Photo: outdoor concert stage with a cheering crowd" points="403,10 805,110 805,332 403,332" fill="url(#outdoor-tone)"/>
    <polygon role="img" aria-label="Photo: church sanctuary with projection screen and A/V system" points="806,10 1200,100 1200,332 806,332" fill="url(#church-tone)"/>
  </svg>

  <footer class="caption-band">
    <span>Lights and sound system for indoor concerts</span>
    <span>Lights and sound system for outdoor concerts</span>
    <span>A/V systems for churches</span>
  </footer>

</main>
</body>
</html>
```